Fresh new and cool frozen burger box! Come be a part of an amazing project!

Crust Fins and Melts restaurant is expanding into the frozen foods market!
please check out our website to understand the vibe of the company
https://brivanta.ca
this is a line of premium Halal meat, we want to stress our top-notch quality.
we like the orange colours so see what you can do with them. (maybe white and orange combo)
you have lots of creative freedom here, feel free to use the burger photo I am attaching or any image off the website.
logo should be nice and visible.
we want this packaging to really stand out and be special.
Come be a part of an amazing project!
Target Market(s)
Muslim Flails, looking of a quality meat burger. mostly already familiar with our brand
Industry/Entity Type
Frozen food
Look and feel

```html
<!DOCTYPE html>
<html lang="en">
<head>
<meta charset="utf-8">
<title>Brivanta Frozen Burgers – Box Front</title>
<link rel="stylesheet" href="https://fonts.googleapis.com/css2?family=Anton&family=Roboto+Condensed:wght@600;700&display=swap">
<style>
  :root {
    --page: #f4f1ee;
    --peach: #f6d7ae;
    --peach-light: #f9e2c3;
    --orange: #ef8a1e;
    --orange-deep: #e4761a;
    --orange-light: #f6a53c;
    --ink: #1e1a17;
    --brown: #3a2412;
    --white: #ffffff;
  }
  * { margin: 0; padding: 0; box-sizing: border-box; }
  html, body { width: 1200px; height: 900px; overflow: hidden; background: var(--page); }
  .canvas { position: relative; width: 1200px; height: 900px; }
  .box-front {
    position: absolute; left: 60px; top: 75px; width: 1080px; height: 750px;
    background: linear-gradient(180deg, var(--peach-light), var(--peach));
    overflow: hidden;
  }
  .edge-stripe {
    position: absolute; left: 0; top: 0; width: 70px; height: 100%;
    background: linear-gradient(90deg, var(--orange-deep), var(--orange-light));
  }
  .brand-panel {
    position: absolute; left: 150px; top: 0; width: 470px; height: 520px;
    background: linear-gradient(180deg, var(--orange-deep), var(--orange));
    display: flex; flex-direction: column; align-items: center;
  }
  .brand-mark {
    width: 150px; height: 150px; margin-top: 60px; border-radius: 50%;
    background: var(--white);
  }
  .brand-name {
    margin-top: 60px; font-family: "Anton", sans-serif; font-size: 118px;
    line-height: 1; letter-spacing: 2px; color: var(--white);
  }
  .brand-tagline {
    margin-top: 18px; font-family: "Roboto Condensed", sans-serif; font-weight: 700;
    font-size: 40px; color: var(--brown);
  }
  .product-title {
    position: absolute; left: 190px; top: 560px; width: 420px;
    font-family: "Roboto Condensed", sans-serif; color: var(--ink); text-align: center;
  }
  .product-title .kind { display: block; font-weight: 600; font-size: 54px; line-height: 1; }
  .product-title .item {
    display: flex; align-items: flex-end; justify-content: center; gap: 8px;
    font-weight: 700; font-size: 88px; line-height: 1;
  }
  .product-title .dash { display: inline-block; width: 48px; height: 7px; background: var(--ink); margin-bottom: 10px; }
  .burger-photo {
    position: absolute; right: 20px; top: 20px; width: 470px; height: 700px;
    border-radius: 48% 48% 42% 42%;
    background: radial-gradient(ellipse at 50% 40%, #e9a55a 0%, #c96a2c 40%, #8a4a24 62%, #6aa842 75%, rgba(246,215,174,0) 88%);
  }
  .bottom-swoosh { position: absolute; left: 0; bottom: 0; width: 1080px; height: 150px; }
</style>
</head>
<body>
<main class="canvas">
  <section class="box-front">
    <div class="edge-stripe"></div>
    <div class="burger-photo" role="img" aria-label="Photo of a stacked burger with sesame bun, lettuce, tomato, bacon, cheese and beef patty, with ingredients flying above"></div>
    <svg class="bottom-swoosh" viewBox="0 0 1080 150" preserveAspectRatio="none" aria-hidden="true">
      <path d="M0 150 L0 120 Q420 150 720 40 Q880 -10 1080 10 L1080 150 Z" fill="var(--orange)"/>
    </svg>
    <div class="brand-panel">
      <div class="brand-mark"></div>
      <h1 class="brand-name">BRIVANTA</h1>
      <p class="brand-tagline">Premium Halal Meat</p>
    </div>
    <h2 class="product-title">
      <span class="kind">Frozen</span>
      <span class="item"><span class="dash"></span>Burgers<span class="dash"></span></span>
    </h2>
  </section>
</main>
</body>
</html>
```